Education Certificate

We need a modern yet professional Certificate for those who successfully pass / complete our online Training course.

There are various courses but ONE certificate design required.

the certificate needs to look extremely professional and of value.

```html
<!DOCTYPE html>
<html lang="en">
<head>
<meta charset="utf-8">
<title>Certificate of Appreciation</title>
<link href="https://fonts.googleapis.com/css2?family=Roboto:wght@400;500&family=Great+Vibes&family=Mrs+Saint+Delafield&display=swap" rel="stylesheet">
<style>
  :root {
    --navy: #1f2f6b;
    --navy-leaf: #2c48a3;
    --yellow: #f5d418;
    --paper: #f7f7f7;
    --ink: #111111;
    --white: #ffffff;
    --rule: #1f2f6b;
  }
  * { margin: 0; padding: 0; box-sizing: border-box; }
  html, body { width: 1200px; height: 927px; overflow: hidden; background: var(--paper); }
  .certificate {
    position: relative;
    width: 1200px;
    height: 927px;
    background: var(--paper);
    font-family: "Roboto", Arial, sans-serif;
    overflow: hidden;
  }
  .certificate__backdrop { position: absolute; inset: 0; width: 1200px; height: 927px; }
  .brand {
    position: absolute;
    left: 542px; top: 64px;
    width: 268px; height: 138px;
    background: var(--navy);
    color: var(--white);
    font-weight: 400;
    font-size: 26px;
    line-height: 30px;
    padding: 10px 0 0 22px;
    letter-spacing: 0.3px;
  }
  .title {
    position: absolute;
    left: 0; width: 100%;
    top: 282px;
    text-align: center;
    color: var(--navy);
    font-size: 104px;
    font-weight: 400;
    line-height: 1;
    letter-spacing: 0.5px;
  }
  .subtitle {
    position: absolute;
    left: 0; width: 100%;
    top: 384px;
    text-align: center;
    color: var(--yellow);
    font-size: 52px;
    font-weight: 400;
    line-height: 1;
  }
  .recipient {
    position: absolute;
    left: 324px; width: 553px;
    top: 490px;
    text-align: center;
    font-family: "Great Vibes", cursive;
    font-size: 96px;
    line-height: 1;
    color: var(--ink);
  }
  .recipient__rule {
    position: absolute;
    left: 324px; top: 588px;
    width: 553px; height: 1px;
    background: var(--ink);
  }
  .statement {
    position: absolute;
    left: 0; width: 100%;
    top: 642px;
    text-align: center;
    color: var(--navy);
    font-size: 18px;
  }
  .course {
    position: absolute;
    left: 0; width: 100%;
    top: 677px;
    text-align: center;
    color: var(--navy);
    font-size: 20px;
    line-height: 28px;
  }
  .date-block {
    position: absolute;
    left: 76px; top: 830px;
    width: 310px;
    text-align: center;
    color: var(--white);
  }
  .date-block__value { font-size: 20px; padding-bottom: 8px; border-bottom: 1px solid var(--white); }
  .date-block__label { font-size: 20px; margin-top: 12px; }
  .signature-block {
    position: absolute;
    left: 862px; top: 780px;
    width: 304px;
    text-align: center;
    color: var(--navy);
  }
  .signature-block__mark {
    font-family: "Mrs Saint Delafield", cursive;
    font-size: 62px;
    line-height: 82px;
    color: var(--ink);
    border-bottom: 1px solid var(--rule);
  }
  .signature-block__label { font-size: 20px; margin-top: 10px; }
</style>
</head>
<body>
<main class="certificate">
  <svg class="certificate__backdrop" viewBox="0 0 1200 927" xmlns="http://www.w3.org/2000/svg" aria-hidden="true">
    <path class="panel-navy" d="M0,0 C60,360 260,760 595,927 L0,927 Z" fill="#1f2f6b" stroke="#111111" stroke-width="1.5"/>
    <path class="swoosh-yellow" d="M590,927 C860,870 1080,700 1200,477 L1200,600 C1090,770 880,905 700,927 Z" fill="#f5d418"/>
  </svg>
  <svg class="laurel" style="position:absolute;left:0;top:250px" width="330" height="540" viewBox="0 0 330 540" role="img" aria-label="Decorative laurel branch in soft blue">
    <path d="M20,0 C80,120 150,330 320,520 L300,530 C120,360 40,160 0,30 Z" fill="#2c48a3" opacity="0.55"/>
  </svg>

  <div class="brand">GLOBAL<br>SERVICE<br>QUALITY<br>ACADEMY</div>

  <h1 class="title">CERTIFICATE</h1>
  <p class="subtitle">OF APPRECIATION</p>

  <p class="recipient">Name Surname</p>
  <div class="recipient__rule"></div>

  <p class="statement">has successfully completed the training course.</p>
  <p class="course">Customer Experience<br>Service Excellence</p>

  <div class="date-block">
    <p class="date-block__value">21.03.2024. United Kingdom</p>
    <p class="date-block__label">Date</p>
  </div>

  <div class="signature-block">
    <p class="signature-block__mark">Mentor Name</p>
    <p class="signature-block__label">Signature</p>
  </div>
</main>
</body>
</html>
```